Vendro Sahel - Website Design Brief

Web Design Brief

VENDRO SAHEL
WEBSITE DESIGN BRIEF

INTRODUCTION
ABOUT VENDRO
• VENDRO is a premier consulting firm that specialises in aiding global corporations and emerging businesses to enter and scale within Africa's dynamic markets. Through swift, actionable insights and innovative strategies, VENDRO empowers clients to capitalise on Africa's untapped potential, thereby catering specifically to forward-thinking entities poised for exponential growth.

TASK DESCRIPTION
• Develop a 5-page website for VENDRO.
• The primary goal is to present a clear and concise picture of our consulting firm, its Africa-centric experience, and its offerings to multinational clients looking for a professional partner to penetrate African markets or reclaim lost market share.

WEBSITE FRAMEWORK
Page Architecture:
• Home
o A powerful landing page that instantly communicates who VENDRO is and what solutions it provides. Incorporate impactful visuals and calls-to-action.
• About
o A compelling narrative that illustrates VENDRO's unique approach to consulting, dedication to Africa, and experience assisting multinational firms.
• Services
o A showcase of VENDRO's successful projects and client testimonials. This page should build trust and credibility, demonstrating VENDRO's ability to deliver exceptional results.
• Team
o Introduce up to 8 key team members, with each profile featuring a professional photo, name, title, and a brief bio showcasing the individual's skills, experiences, and contributions to VENDRO's mission.
• Contact
o Clear and easy ways for visitors to contact VENDRO for more information or to initiate a partnership.
• Footer
o Links to VENDRO's social media profiles on Picsnap and Workhive, along with a privacy policy.
o Social links
o Picsnap: https://www.instagram.com/vendrosahel/
o Workhive: https://www.linkedin.com/company/vendrosahel/
o Privacy Policy
o Insert placeholder "lorem ipsum" text.
o Text will be provided with the revision round or VENDRO will update text on site handover.

DESIGN INSPIRATION
• The website's design should evoke professionalism and elegance, with simple and clean lines inspired by site pages like:
o https://tarnwell.example/
o https://tarnwell.example/services/
o One aspect we particularly appreciate is how visitors can easily navigate by scrolling down to find what they're looking for and see everything they need to in an intuitive way on the home page
o What we don’t like about this site is how they navigate from the home page to other random pages – we like about to take you to the about page, and so on.

Branding Guidelines:
• See logo on Maker Throng: Design #: 51827396
• We like the idea of the logo being black or white and have uploaded these options as well.
• Monochrome themes, with spots or splash of colour to highlight something is a style we appreciate.

Website Objectives and Goals:
• Our website's primary goal is to create a strong online presence, acting as a hub for potential clients to discover our credibility, reliability, and our ability to deliver exceptional results. It's essential that our website portrays professionalism, instils trustworthiness, and showcases our sincere dedication to Africa.

Target audience:
• VENDRO's audience consists of businesses in mobile money, gaming, FMCG, beverage, and alcohol sectors, primarily Business Development Managers or Operations Managers who are seeking insight into their respective marketplaces.

Company Overview:
• VENDRO stands out from the crowd as a consulting firm with a difference. Our dynamic team is fully dedicated to one mission: brand development within Africa.
• Unlike other companies that focus solely on online connectivity, we recognize the tremendous value in embracing the vibrant street culture that makes Africa so unique. Community engagement, empowerment, and expansion are at the forefront of everything we do.
• we recognize that unlocking business growth starts with a deep understanding of consumer behavior. It is this understanding that bridges the gap between companies and the communities that drive the cash economy. Our purpose is to reconnect businesses with the vibrant pulse of these essential local markets, injecting fresh vitality into their brands and propelling them towards resounding success in Africa.

Development to include:
• Basic SEO Setup:
o The website should be optimized for search engines, incorporating keywords, meta tags, and alt tags for images.
• Searchly Metrics Setup.
o To track website traffic and user behaviour for ongoing optimization.
• Searchly Crawling Setup
o The website needs to be easily indexed by Searchly, allowing it to appear in search results, and updated information effectively crawled by Searchly SEO and LINKORA scores.

PAGE CONTENT:
Home Page
• Background
o Option #1
o 4K video on home page, running on loop
o Bold Statement Text over Video
o Option #2
o Still Image
o Animated text making bold statement (e.g. our motto)

• Sections
o Contrast colour blocks or a way of making it clear that the next topic is a new topic.
o 5 sections
1. Home Main - Video + bold statement text
2. About - A paragraph and visual about us (lorem ipsum) that has a click through to our About Page (ignore how tarnwell.example navigate, we think this is too complicated for our needs)
3. Services – communicated in some simple and powerful ways (we leave this open to you) – but keeping in mind it needs to be concise and professional.
4. Other - Something about our process that makes us unique (lorem ipsum text) and a placeholder image/animation.
5. Contact – a call-to-action button that takes you to our contact, but showcases a mobile number and email address.
6. Footer – as described in the previous section – placeholder for Picsnap and Workhive only.

About Page
• Don’t reference tarnwell.example for this page.
• Main Section
o Bold statements and images
• History Section
o A story about us and our past
• Final Section
o Some of our comments and final thoughts

Services Page
• How https://tarnwell.example/services/ is laid out is great – we prefer a light theme.
• 6 - 8 x icons with headings and a brief description text box, and a read more drop down – all as placeholders to be edited later.
• For ease of direction for this page, look to the link shared above.

Team
• Add Placeholders for up to 8 team members (we only have 4 now):
o Image placeholder
o Name placeholder
o Title placeholder
o Short Bio (lorem ipsum)

Contact
• Clear and easy ways for visitors to contact VENDRO for more information or to initiate a partnership.

• Insert placeholder "lorem ipsum" text, we will provide the text with our revision round.
o Ideally an easy form process that gives the user some options or dropdowns to complete before submission – up to 3 would be sufficient.
o Require their name and contact details.

NOTE: Images to follow:

Target Market(s)

VENDRO's audience consists of businesses in mobile money, gaming, FMCG, beverage, and alcohol sectors, primarily Business Development Managers or Operations Managers who are seeking insight into their respective marketplaces.

Industry/Entity Type

VENDRO is a premier consulting firm that specialises in aiding global corporations and emerging businesses to enter and scale within Africa's dynamic markets

Coding

Coded - Design and coding required

Number of Pages Required

5+ page

Font styles to use
Sans Serif
Other font styles liked:
• Poppins Font Family

Colors

Designer to choose colors to be used in the design.

Requirements
Must have
• The primary goal is to present a clear and concise picture of our consulting firm, and it's specialisation in Africa - smooth and crisp UI with animations or transitions that imply we know our way around tecchnology is always helpful - but a Clean and responsive UI is most important.
Nice to have
• Reactive and animated transitions through sections or pages - not overdone - adds a professional feel to the site
Should not have
• We don't want too many colours, and we don't want it too dark - we want a monochrome theme, with accents of colour when relevant

```html
<!DOCTYPE html>
<html lang="en">
<head>
<meta charset="utf-8">
<title>VENDRO — Consulting for African Markets</title>
<link rel="stylesheet" href="https://fonts.googleapis.com/css2?family=Josefin+Sans:wght@300;400;600;700&display=swap">
<style>
:root{
  --blue:#0a6bbf;
  --blue-dark:#0859a0;
  --ink:#111;
  --muted:#8a8a8a;
  --line:#bdbdbd;
  --white:#fff;
  --soft:#e9e9e9;
}
*{box-sizing:border-box;margin:0;padding:0}
html,body{width:1200px;height:3952px;overflow:hidden}
body{position:relative;background:var(--white);font-family:"Josefin Sans",sans-serif;color:var(--ink)}
.abs{position:absolute}
a{color:inherit;text-decoration:none}

/* hero */
.hero{left:0;top:0;width:1200px;height:611px;background:var(--blue)}
.logo{display:flex;align-items:center;gap:8px;font-weight:700;color:var(--white)}
.logo-mark{width:22px;height:22px;border:3px solid var(--white)}
.nav-logo{left:101px;top:20px;font-size:26px}
.nav-link{top:26px;font-size:16px;color:var(--white)}
.btn-outline{left:976px;top:15px;width:129px;height:40px;border:2px solid var(--white);border-radius:20px;color:var(--white);font-size:16px;display:flex;align-items:center;justify-content:center}
.hero-title{left:0;width:1200px;top:158px;text-align:center;color:var(--white);font-size:41px;font-weight:600;line-height:51px;letter-spacing:.5px}
.hero-sub{left:0;width:1200px;top:276px;text-align:center;color:var(--white);font-size:14px;font-weight:300;line-height:20px}
.btn-pill{display:flex;align-items:center;justify-content:center;border-radius:22px;font-size:16px}
.btn-start{left:450px;top:363px;width:142px;height:42px;background:var(--white);color:var(--blue)}
.btn-learn{left:615px;top:374px;font-size:17px;color:var(--white)}
.video{left:77px;top:477px;width:1048px;height:576px;background:linear-gradient(180deg,#7d7d7d 0%,#a5a5a5 45%,#6a6a6a 100%)}
.play{left:568px;top:734px}

/* services */
.eyebrow{font-size:15px;color:var(--blue)}
.section-title{font-size:41px;font-weight:700;letter-spacing:.5px}
.service-desc{left:89px;top:1226px;width:520px;font-size:16px;font-weight:300;line-height:22px;color:var(--muted)}
.card{width:300px}
.card-icon{width:54px;height:54px;background:var(--soft);display:flex;align-items:center;justify-content:center}
.card-icon.active{background:var(--blue)}
.card h3{margin-top:12px;font-size:21px;font-weight:600;letter-spacing:.3px}
.card p{margin-top:13px;font-size:12px;line-height:17px;font-weight:300;color:#555}
.card .more{display:block;margin-top:7px;font-size:11px;font-weight:600}
.btn-view{left:525px;top:1792px;width:142px;height:43px;background:var(--blue);color:var(--white);font-size:15px}

/* about */
.about-photo{left:0;top:1943px;width:600px;height:420px;background:linear-gradient(135deg,#5a5a5a,#b0b0b0 55%,#4a4a4a)}
.about-panel{left:600px;top:1943px;width:600px;height:420px;background:var(--blue);color:var(--white)}
.about-panel .eyebrow{color:var(--white)}
.about-text{font-size:15px;font-weight:300;line-height:22px;width:495px}
.btn-read{left:40px;top:354px;width:143px;height:40px;background:var(--white);color:var(--blue);font-size:15px}

/* process */
.step-num{font-size:35px;color:var(--blue)}
.step-title{font-size:21px;margin-top:4px}
.step-desc{font-size:10px;line-height:13px;color:#555;width:140px;margin-top:6px;font-weight:300}

/* contact */
.talk{left:183px;top:3084px;width:578px;height:448px;background:var(--white);box-shadow:0 6px 24px rgba(0,0,0,.12)}
.talk h2{position:absolute;left:16px;top:26px;font-size:41px;font-weight:700}
.talk .intro{position:absolute;left:16px;top:90px;width:500px;font-size:16px;line-height:22px;font-weight:300;color:var(--muted)}
.field{position:absolute;height:30px;border-bottom:1.5px solid var(--line);font-size:13px;color:var(--muted);font-weight:300}
.btn-submit{left:412px;top:389px;width:143px;height:38px;background:var(--blue);color:var(--white);font-size:15px}
.contact-card{left:761px;top:3084px;width:279px;height:448px;background:var(--blue);color:var(--white)}
.contact-card h3{position:absolute;left:23px;top:40px;font-size:26px;font-weight:600}
.contact-row{position:absolute;left:23px;display:flex;gap:12px;font-size:16px;font-weight:300;line-height:22px}

/* footer */
.footer{left:0;top:3621px;width:1200px;height:331px;background:var(--blue);color:var(--white)}
.footer-logo{left:87px;top:52px;font-size:36px}
.footer-about{left:87px;top:115px;width:260px;font-size:15px;line-height:22px;font-weight:300}
.footer h4{position:absolute;top:50px;font-size:27px;font-weight:600;letter-spacing:.5px}
.footer ul{position:absolute;top:98px;list-style:none;font-size:15px;font-weight:300;line-height:29px}
.news-input{left:895px;top:108px;width:149px;height:30px;background:var(--white);font-size:12px;color:#bbb;padding:9px 10px;font-weight:300}
.news-btn{left:1044px;top:108px;width:65px;height:30px;background:#000;color:var(--white);font-size:14px;display:flex;align-items:center;justify-content:center;font-weight:600}
.social{font-size:14px;font-weight:400;display:flex;gap:14px}
.footer-rule{left:0;top:280px;width:1200px;height:1px;background:rgba(255,255,255,.5)}
.copyright{left:0;top:300px;width:1200px;text-align:center;font-size:16px;font-weight:300}
</style>
</head>
<body>

<!-- HERO -->
<section class="abs hero"></section>
<a class="abs logo nav-logo" href="#"><span class="logo-mark"></span>VENDRO</a>
<a class="abs nav-link" style="left:425px" href="#">Home</a>
<a class="abs nav-link" style="left:516px" href="#">About us</a>
<a class="abs nav-link" style="left:631px" href="#">Service &#8964;</a>
<a class="abs nav-link" style="left:732px" href="#">Team</a>
<a class="abs btn-outline" href="#">Contact</a>

<h1 class="abs hero-title">Lorem Ipsum is simply dummy text<br>printing and typesetting</h1>
<p class="abs hero-sub">Lorem Ipsum is simply dummy text of the printing and typesetting<br>industry. Lorem Ipsum has been the industry'</p>
<a class="abs btn-pill btn-start" href="#">Get Started &rarr;</a>
<a class="abs btn-learn" href="#">Learn More</a>

<div class="abs video" role="img" aria-label="Black and white video still of a busy city street market with traffic"></div>
<svg class="abs play" width="64" height="64" viewBox="0 0 64 64" aria-hidden="true">
  <circle cx="32" cy="32" r="30" fill="#fff"/>
  <path d="M26 21 L44 32 L26 43 Z" fill="#222"/>
</svg>

<!-- SERVICES -->
<p class="abs eyebrow" style="left:89px;top:1137px">— Service</p>
<h2 class="abs section-title" style="left:89px;top:1170px">Our service we can help you</h2>
<p class="abs service-desc">Lorem Ipsum is simply dummy text of the printing and typesetting industry. Lorem Ipsum has</p>

<article class="abs card" style="left:103px;top:1335px">
  <div class="card-icon"><svg width="32" height="28" viewBox="0 0 32 28"><g fill="none" stroke="#333" stroke-width="1.5"><rect x="3" y="16" width="5" height="10"/><rect x="11" y="12" width="5" height="14"/><rect x="19" y="8" width="5" height="18"/><path d="M3 10 L12 5 L18 8 L28 2"/></g></svg></div>
  <h3>Identify Growth Pathways</h3>
  <p>Lorem Ipsum is simply dummy text of the printing and typesetting industry. Lorem Ipsum has been the industry's standard</p>
  <a class="more" href="#">Read More &rarr;</a>
</article>
<article class="abs card" style="left:445px;top:1335px">
  <div class="card-icon active"><svg width="32" height="28" viewBox="0 0 32 28"><g fill="none" stroke="#fff" stroke-width="1.5"><circle cx="10" cy="8" r="4"/><circle cx="22" cy="8" r="4"/><path d="M3 24 C3 15 17 15 17 24 M15 24 C15 15 29 15 29 24"/></g></svg></div>
  <h3>Empower Employees</h3>
  <p>Lorem Ipsum is simply dummy text of the printing and typesetting industry. Lorem Ipsum has been the industry's standard</p>
  <a class="more" href="#">Read More &rarr;</a>
</article>
<article class="abs card" style="left:787px;top:1335px">
  <div class="card-icon"><svg width="32" height="28" viewBox="0 0 32 28"><g fill="none" stroke="#333" stroke-width="1.5"><rect x="6" y="2" width="20" height="14"/><rect x="3" y="12" width="9" height="14"/><path d="M12 20 H22"/></g></svg></div>
  <h3>Revolutionize Experiences</h3>
  <p>Lorem Ipsum is simply dummy text of the printing and typesetting industry. Lorem Ipsum has been the industry's standard</p>
  <a class="more" href="#">Read More &rarr;</a>
</article>
<article class="abs card" style="left:103px;top:1568px">
  <div class="card-icon"><svg width="32" height="28" viewBox="0 0 32 28"><g fill="none" stroke="#333" stroke-width="1.5"><circle cx="10" cy="6" r="3"/><circle cx="16" cy="5" r="3"/><circle cx="22" cy="6" r="3"/><path d="M3 22 Q10 16 18 20 L28 16 M3 26 H26"/></g></svg></div>
  <h3>Drive Customer Demand</h3>
  <p>Lorem Ipsum is simply dummy text of the printing and typesetting industry. Lorem Ipsum has been the industry's standard</p>
  <a class="more" href="#">Read More &rarr;</a>
</article>
<article class="abs card" style="left:445px;top:1568px">
  <div class="card-icon"><svg width="32" height="28" viewBox="0 0 32 28"><g fill="none" stroke="#333" stroke-width="1.5"><circle cx="16" cy="5" r="3"/><path d="M16 8 L7 25 H25 Z M11 18 H21"/></g></svg></div>
  <h3>Reimagine Brands</h3>
  <p>Lorem Ipsum is simply dummy text of the printing and typesetting industry. Lorem Ipsum has been the industry's standard</p>
  <a class="more" href="#">Read More &rarr;</a>
</article>
<article class="abs card" style="left:787px;top:1568px">
  <div class="card-icon"><svg width="32" height="28" viewBox="0 0 32 28"><g fill="none" stroke="#333" stroke-width="1.5"><circle cx="14" cy="15" r="10"/><circle cx="14" cy="15" r="5"/><path d="M14 15 L27 3"/></g></svg></div>
  <h3>Identify Growth Pathways</h3>
  <p>Lorem Ipsum is simply dummy text of the printing and typesetting industry. Lorem Ipsum has been the industry's standard</p>
  <a class="more" href="#">Read More &rarr;</a>
</article>
<a class="abs btn-pill btn-view" href="#">View More &nbsp;&rarr;</a>

<!-- ABOUT -->
<div class="abs about-photo" role="img" aria-label="Black and white photo of people at a street-side mobile money kiosk"></div>
<section class="abs about-panel">
  <p class="abs eyebrow" style="left:40px;top:47px">— About us</p>
  <h2 class="abs section-title" style="left:40px;top:75px">Who we are ?</h2>
  <p class="abs about-text" style="left:31px;top:152px">Lorem Ipsum is simply dummy text of the printing and typesetting industry. Lorem Ipsum has been the industry's standard dummy text ever since the 1500s Lorem Ipsum has been the industry's standard dummy text ever since the 1500so be better</p>
  <p class="abs about-text" style="left:31px;top:253px">when an unknown printer took a galley of type and scrambled it to make a type specimen book</p>
  <a class="abs btn-pill btn-read" href="#">Read More &nbsp;&rarr;</a>
</section>

<!-- PROCESS -->
<p class="abs eyebrow" style="left:0;width:1200px;text-align:center;top:2476px">— Our Process</p>
<h2 class="abs section-title" style="left:0;width:1200px;text-align:center;top:2494px">Key features</h2>

<svg class="abs" style="left:0;top:2660px" width="1200" height="260" viewBox="0 2660 1200 260" aria-hidden="true">
  <path d="M164 2754 L339 2831 L513 2754 L686 2831 L861 2754 L1034 2831" fill="none" stroke="var(--blue)" stroke-width="34" stroke-linejoin="round"/>
  <g fill="#fff" stroke="var(--blue)" stroke-width="7">
    <circle cx="164" cy="2754" r="70"/><circle cx="339" cy="2831" r="70"/>
    <circle cx="513" cy="2754" r="70"/><circle cx="686" cy="2831" r="70"/>
    <circle cx="861" cy="2754" r="70"/><circle cx="1034" cy="2831" r="70"/>
  </g>
  <g fill="none" stroke="#222" stroke-width="2" stroke-linecap="round">
    <path d="M339 2730 V2745 M686 2730 V2745 M1034 2730 V2745"/>
    <path d="M164 2840 V2855 M513 2840 V2855 M861 2840 V2855"/>
    <!-- bulb -->
    <circle cx="164" cy="2748" r="16"/><path d="M157 2766 V2776 H171 V2766 M158 2781 H170 M164 2740 V2756"/>
    <path d="M140 2730 L146 2736 M188 2730 L182 2736 M164 2722 V2728 M134 2750 H140 M188 2750 H194"/>
    <!-- rocket -->
    <path d="M339 2798 C326 2812 326 2840 331 2856 H347 C352 2840 352 2812 339 2798 Z M331 2840 L321 2858 L331 2856 M347 2840 L357 2858 L347 2856"/><circle cx="339" cy="2826" r="5"/>
    <!-- bar chart -->
    <path d="M482 2786 V2770 H492 V2786 M497 2786 V2762 H507 V2786 M512 2786 V2754 H522 V2786 M527 2786 V2746 H537 V2786 M476 2786 H544 M484 2750 L505 2734 L517 2742 L538 2724"/>
    <!-- clock -->
    <circle cx="686" cy="2836" r="28"/><path d="M686 2818 V2836 L698 2844 M664 2806 L672 2812 M708 2806 L700 2812 M678 2804 H694"/>
    <!-- coins -->
    <ellipse cx="840" cy="2770" rx="12" ry="4"/><ellipse cx="840" cy="2762" rx="12" ry="4"/><ellipse cx="861" cy="2770" rx="12" ry="4"/><ellipse cx="861" cy="2762" rx="12" ry="4"/><ellipse cx="882" cy="2770" rx="12" ry="4"/><ellipse cx="882" cy="2762" rx="12" ry="4"/>
    <circle cx="850" cy="2742" r="9"/><circle cx="872" cy="2738" r="9"/>
    <!-- trophy -->
    <path d="M1016 2806 H1052 V2824 C1052 2838 1016 2838 1016 2824 Z M1016 2812 H1006 C1006 2826 1016 2828 1016 2828 M1052 2812 H1062 C1062 2826 1052 2828 1052 2828 M1034 2836 V2848 M1022 2856 H1046 V2848 H1022 Z"/>
    <path d="M1034 2812 L1037 2818 L1043 2818 L1038 2822 L1040 2828 L1034 2824 L1028 2828 L1030 2822 L1025 2818 L1031 2818 Z"/>
  </g>
</svg>

<div class="abs" style="left:264px;top:2596px"><p class="step-num">02</p><p class="step-title">Start Moving</p><p class="step-desc">Lorem ipsum dolor sit amet, consectetuer adipiscing elit diam nonummy nibh euismod</p></div>
<div class="abs" style="left:614px;top:2596px"><p class="step-num">04</p><p class="step-title">Take Time</p><p class="step-desc">Lorem ipsum dolor sit amet, consectetuer adipiscing elit diam nonummy nibh euismod</p></div>
<div class="abs" style="left:968px;top:2596px"><p class="step-num">06</p><p class="step-title">The Award</p><p class="step-desc">Lorem ipsum dolor sit amet, consectetuer adipiscing elit diam nonummy nibh euismod</p></div>
<div class="abs" style="left:95px;top:2876px"><p class="step-num">01</p><p class="step-title">A Good Idea</p><p class="step-desc">Lorem ipsum dolor sit amet, consectetuer adipiscing elit diam nonummy nibh euismod</p></div>
<div class="abs" style="left:445px;top:2876px"><p class="step-num">03</p><p class="step-title">Increase</p><p class="step-desc">Lorem ipsum dolor sit amet, consectetuer adipiscing elit diam nonummy nibh euismod</p></div>
<div class="abs" style="left:799px;top:2876px"><p class="step-num">05</p><p class="step-title">Earnings</p><p class="step-desc">Lorem ipsum dolor sit amet, consectetuer adipiscing elit diam nonummy nibh euismod</p></div>

<!-- CONTACT -->
<section class="abs talk">
  <h2>Let's Talk</h2>
  <svg class="abs" style="left:530px;top:40px" width="22" height="16" viewBox="0 0 22 16" aria-hidden="true"><rect width="22" height="16" rx="2" fill="#111"/><path d="M1 2 L11 9 L21 2" fill="none" stroke="#fff" stroke-width="1.6"/></svg>
  <p class="intro">Lorem Ipsum is simply dummy text of the printing and typesetting industry. Lorem Ipsum has</p>
  <div class="field" style="left:16px;top:174px;width:213px">First Name</div>
  <div class="field" style="left:254px;top:174px;width:213px">Last Name</div>
  <div class="field" style="left:16px;top:223px;width:213px">Phone</div>
  <div class="field" style="left:254px;top:223px;width:213px">Email</div>
  <div class="field" style="left:16px;top:272px;width:451px">Group or Company</div>
  <div class="field" style="left:16px;top:321px;width:451px">Message</div>
  <a class="abs btn-pill btn-submit" href="#">Submit</a>
</section>
<aside class="abs contact-card">
  <h3>Contact us</h3>
  <div class="contact-row" style="top:108px">
    <svg width="12" height="18" viewBox="0 0 12 18" aria-hidden="true"><rect x="1" y="1" width="10" height="16" rx="2" fill="none" stroke="#fff" stroke-width="1.6"/><circle cx="6" cy="14" r="1" fill="#fff"/></svg>
    <span>+ 123 4566 7890</span></div>
  <div class="contact-row" style="top:152px">
    <svg width="12" height="18" viewBox="0 0 12 18" aria-hidden="true"><path d="M6 17 C6 17 1 10 1 6 A5 5 0 0 1 11 6 C11 10 6 17 6 17 Z" fill="#fff"/><circle cx="6" cy="6" r="2" fill="var(--blue)"/></svg>
    <span>Lorem Ipsum is simply<br>dummy text</span></div>
  <div class="contact-row social" style="top:218px"><span>Picsnap</span><span>Workhive</span></div>
</aside>

<!-- FOOTER -->
<footer class="abs footer">
  <a class="abs logo footer-logo" href="#"><span class="logo-mark" style="width:30px;height:30px"></span>VENDRO</a>
  <p class="abs footer-about">Lorem Ipsum is simply dummy text of the printing and typesetting industry. Lorem Ipsum has been the industry's standard</p>
  <h4 style="left:442px">Quick Line</h4>
  <ul style="left:442px"><li>Home</li><li>About us</li><li>Service</li><li>Team</li><li>Contact</li></ul>
  <h4 style="left:660px">Support</h4>
  <ul style="left:660px"><li>Terms &amp; conditions</li><li>Privacy policy</li><li>Terms if use</li></ul>
  <h4 style="left:895px">Newsletters</h4>
  <div class="abs news-input">your email</div>
  <div class="abs news-btn">Submit</div>
  <div class="abs social" style="left:895px;top:161px"><span>Picsnap</span><span>Workhive</span></div>
  <div class="abs footer-rule"></div>
  <p class="abs copyright">Copyright©2023 All Rights Reserved VENDRO</p>
</footer>

</body>
</html>
```